SUMMIT GATHERING 2021. August 20th -22nd.

The Hosts of the conference: Grace Tabernacle-Pastors Ron n Della ( Picture with two persons)

Guest Minister: Bishop Lucinda Okotieno. (Cedar Ridge Awakening)

Venue:
Sealand Gateway Lodgeview. 4817 North 239th Avenue Seattle, WA 98174.

Conference times.
Friday August 20th 6pm-8:30pm
Saturday August 21st. 6pm-8:30pm

Sunday August 22nd 10am-1pm
“ CHURCH RENEWAL GATHERING”

5pm-7:30pm
TWOFOLD SURGE GATHERING.

Target Market(s)

18-55

Industry/Entity Type

Religious/ Entertainment.

Requirements
Must have
• A highlight of the Relaunch service on Sunday August 22nd 5pm-7:30pm.
Nice to have
• Excellent ideas….

```html
<!DOCTYPE html>
<html lang="en">
<head>
<meta charset="utf-8">
<title>Summit Gathering 2021</title>
<link rel="stylesheet" href="https://fonts.googleapis.com/css2?family=Montserrat:wght@600;700;800;900&family=Oswald:wght@300;400;500&display=swap">
<style>
  :root {
    --navy: #13283d;
    --navy-deep: #0c1b2b;
    --navy-soft: #1a3550;
    --teal: #1aa39a;
    --teal-light: #2fc7b9;
    --teal-dark: #0f7f7a;
    --white: #ffffff;
    --ink-soft: #e8eef3;
  }
  * { margin: 0; padding: 0; box-sizing: border-box; }
  html, body { width: 848px; height: 1200px; overflow: hidden; background: var(--navy-deep); }
  .poster {
    position: relative;
    width: 848px;
    height: 1200px;
    overflow: hidden;
    color: var(--white);
    background:
      radial-gradient(ellipse 420px 520px at 120px 560px, var(--navy-soft) 0%, transparent 70%),
      radial-gradient(ellipse 380px 300px at 760px 760px, #183149 0%, transparent 70%),
      linear-gradient(180deg, #112538 0%, var(--navy) 50%, var(--navy-deep) 100%);
    font-family: "Oswald", sans-serif;
  }
  .shapes { position: absolute; inset: 0; }
  .dates {
    position: absolute; top: 56px; left: 64px; width: 727px;
    display: flex; justify-content: space-between;
    font-family: "Montserrat", sans-serif; font-weight: 700; font-size: 16px;
  }
  .subtitle {
    position: absolute; top: 236px; left: 171px; width: 500px;
    display: flex; justify-content: space-between;
    font-family: "Montserrat", sans-serif; font-weight: 800; font-size: 27px;
  }
  .year {
    position: absolute; top: 262px; left: 482px;
    font-family: "Oswald", sans-serif; font-weight: 400; font-size: 66px;
    letter-spacing: 12px; line-height: 1;
  }
  .label {
    position: absolute; display: flex; align-items: center; gap: 14px;
    font-family: "Montserrat", sans-serif; font-weight: 700; font-size: 10px;
    letter-spacing: 7px; text-transform: uppercase;
  }
  .label .rule { display: block; height: 2px; background: var(--white); position: relative; }
  .label .rule::after {
    content: ""; position: absolute; top: -3px; width: 8px; height: 8px;
    border-radius: 50%; background: var(--white);
  }
  .label .rule.lead::after { right: -2px; }
  .label .rule.trail::after { right: -4px; }
  .label-hosts { top: 780px; left: 0; }
  .label-times { top: 914px; left: 0; }
  .label-guest { top: 655px; left: 463px; }
  .label-venue { top: 797px; left: 463px; }
  .hosts {
    position: absolute; top: 810px; left: 68px;
    font-family: "Montserrat", sans-serif; font-weight: 700; font-size: 17px; line-height: 24px;
  }
  .guest {
    position: absolute; top: 680px; left: 463px;
    font-weight: 400; font-size: 24px; line-height: 40px; text-transform: uppercase; color: var(--ink-soft);
  }
  .venue {
    position: absolute; top: 840px; left: 463px; width: 340px;
    font-weight: 400; font-size: 23px; line-height: 36px; text-transform: uppercase; color: var(--ink-soft);
  }
  .times {
    position: absolute; top: 937px; left: 68px;
    font-size: 21px; line-height: 37px; text-transform: uppercase;
  }
  .times .day { font-weight: 400; }
  .times .hours { font-weight: 300; }
  .twofold {
    position: absolute; top: 1034px; left: 71px;
    font-size: 20px; line-height: 33px; text-transform: uppercase;
  }
  .twofold .hours { font-weight: 300; display: block; }
  .twofold .name { font-weight: 500; }
  .sunday {
    position: absolute; top: 1046px; left: 476px;
    font-size: 20px; line-height: 34px; text-transform: uppercase;
  }
  .sunday .day { font-weight: 500; }
  .sunday .hours { font-weight: 300; }
  .sunday .name { font-weight: 500; display: block; }
</style>
</head>
<body>
<main class="poster">
  <svg class="shapes" width="848" height="1200" viewBox="0 0 848 1200" aria-hidden="false">
    <defs>
      <linearGradient id="headline-fill" x1="0" y1="0" x2="0" y2="1">
        <stop offset="0" stop-color="#36cfc0"/>
        <stop offset="1" stop-color="#118a83"/>
      </linearGradient>
      <linearGradient id="hosts-photo" x1="0" y1="0" x2="1" y2="1">
        <stop offset="0" stop-color="#3b3a3a"/>
        <stop offset="0.5" stop-color="#7a6a62"/>
        <stop offset="1" stop-color="#d9d4cf"/>
      </linearGradient>
      <linearGradient id="guest-photo" x1="0" y1="0" x2="0" y2="1">
        <stop offset="0" stop-color="#e9e7e4"/>
        <stop offset="1" stop-color="#6c5a52"/>
      </linearGradient>
    </defs>

    <text class="headline" x="97" y="226" textLength="684" lengthAdjust="spacingAndGlyphs"
          font-family="Montserrat, sans-serif" font-weight="900" font-size="148" fill="url(#headline-fill)">SUMMIT</text>

    <!-- hosts portrait frame -->
    <polygon points="213,252 366,338 366,718 213,804 60,718 60,338" fill="none" stroke="var(--teal)" stroke-width="1.5" stroke-linejoin="round"/>
    <polygon points="213,264 356,345 356,710 213,791 71,710 71,345" fill="url(#hosts-photo)" stroke-linejoin="round"
             role="img" aria-label="Portrait photo of the host pastors, a smiling couple"/>

    <!-- guest portrait frame -->
    <polygon points="610,378 720.9,442 720.9,570 610,634 499.1,570 499.1,442" fill="none" stroke="var(--white)" stroke-width="2" stroke-linejoin="round"/>
    <polygon points="610,388 712.2,447 712.2,565 610,624 507.8,565 507.8,447" fill="var(--teal)" stroke="var(--teal)" stroke-width="10" stroke-linejoin="round"/>
    <polygon points="610,406 696.6,456 696.6,556 610,606 523.4,556 523.4,456" fill="var(--white)" stroke="var(--white)" stroke-width="6" stroke-linejoin="round"/>
    <polygon points="610,418 686,462 686,550 610,594 534,550 534,462" fill="var(--teal-light)" stroke="var(--teal-light)" stroke-width="6" stroke-linejoin="round"/>
    <polygon points="610,426 679,466 679,546 610,586 541,546 541,466" fill="url(#guest-photo)" stroke-linejoin="round"
             role="img" aria-label="Portrait photo of the guest minister, Bishop Lucinda Okotieno"/>

    <!-- venue pin -->
    <path d="M432 788 a8 8 0 0 1 8 8 c0 6 -8 14 -8 14 s-8 -8 -8 -14 a8 8 0 0 1 8 -8z" fill="#e8a33a"/>
    <circle cx="432" cy="796" r="3" fill="var(--navy)"/>

    <!-- sunday highlight -->
    <polygon points="466,1010 552,1060 552,1160 466,1210 380,1160 380,1060" fill="none" stroke="var(--navy-soft)" stroke-width="2" stroke-linejoin="round"/>
    <polygon points="510,999 593,1047 593,1143 510,1191 427,1143 427,1047" fill="var(--teal)" stroke="var(--teal)" stroke-width="14" stroke-linejoin="round"/>
    <line x1="475" y1="1112" x2="848" y2="1112" stroke="var(--white)" stroke-width="2"/>
  </svg>

  <div class="dates"><span>A</span><span>U</span><span>G</span><span>U</span><span>S</span><span>T</span><span>&nbsp;</span><span>2</span><span>0</span><span>T</span><span>H</span><span>&nbsp;</span><span>-</span><span>2</span><span>2</span><span>N</span><span>D</span></div>
  <div class="subtitle"><span>G</span><span>A</span><span>T</span><span>H</span><span>E</span><span>R</span><span>I</span><span>N</span><span>G</span></div>
  <div class="year">2021</div>

  <div class="label label-guest">Guest Minister <span class="rule trail" style="width:90px"></span></div>
  <div class="guest">Bishop Lucinda Okotieno<br>(Cedar Ridge Awakening)</div>

  <div class="label label-venue">Venue <span class="rule trail" style="width:80px"></span></div>
  <div class="venue">Sealand Gateway Lodgeview. 4817 North 239th Avenue Seattle, WA 98174.</div>

  <div class="label label-hosts"><span class="rule lead" style="width:56px"></span>Hosts</div>
  <div class="hosts">Grace Tabernacle-Pastors<br>Ron n Della</div>

  <div class="label label-times"><span class="rule lead" style="width:56px"></span>Conference Times</div>
  <div class="times">
    <div><span class="day">Friday August 20th</span> <span class="hours">6pm-8:30pm</span></div>
    <div><span class="day">Saturday August 21st.</span> <span class="hours">6pm-8:30pm</span></div>
  </div>

  <div class="twofold"><span class="hours">5pm-7:30pm</span><span class="name">Twofold Surge Gathering</span></div>

  <div class="sunday"><span class="day">Sunday August 22nd</span> <span class="hours">10am-1pm</span><span class="name">“ Church Renewal Gathering”</span></div>
</main>
</body>
</html>
```